Business Card Design using new logo

As much as we'd like to think that treating everyone equally is the best strategy for fairness, the reality is that the differences in the lives of women and men have to be taken into account to ensure that organizations, programs, services, and yes, even public policy treat women and men in ways that achieve gender equity.

That's where ParityLumen - fairness metrics insight comes in. Using the data-driven tools of gender analysis, our organization can help anyone determine if gender equity is being achieved - in businesses and organizations, in the planning and implementation of programs and services, and in the development and enforcement of public policy.
Updates

Apologies for the delay - have not had time to finalize the decision.  Should be early this week - probably Tuesday.

Industry/Entity Type

Business

Requirements
Must have
• New Logo for ParityLumen
• Logo plus words "Fairness Metrics Insight"

```html
<!DOCTYPE html>
<html lang="en">
<head>
<meta charset="utf-8">
<title>ParityLumen Business Card</title>
<link href="https://fonts.googleapis.com/css2?family=Open+Sans:wght@400;600;700&display=swap" rel="stylesheet">
<style>
  :root {
    --page-bg: #e9e7e4;
    --card-white: #ffffff;
    --card-dark: #3b3b3c;
    --band-dark: #3d3d3e;
    --accent-orange: #f7931e;
    --line-grey: #9a9a9a;
    --text-dark: #333333;
    --text-light: #f2f2f2;
    --text-muted: #c9c9c9;
  }
  * { box-sizing: border-box; margin: 0; padding: 0; }
  html, body {
    width: 1200px; height: 1200px; overflow: hidden;
    background: var(--page-bg);
    font-family: "Open Sans", Arial, sans-serif;
  }
  .canvas {
    width: 1200px; height: 1200px;
    display: flex; flex-direction: column; align-items: center; justify-content: center;
    gap: 60px;
  }
  .card {
    width: 840px; height: 480px; position: relative; overflow: hidden;
    box-shadow: 0 10px 30px rgba(0,0,0,0.18);
  }

  /* Front */
  .card-front { background: var(--card-white); }
  .front-brand {
    position: absolute; top: 96px; left: 0; right: 0;
    display: flex; flex-direction: column; align-items: center;
  }
  .brand-row { display: flex; align-items: center; gap: 16px; }
  .brand-dot { width: 40px; height: 40px; border-radius: 50%; background: var(--accent-orange); }
  .brand-name { font-weight: 700; font-size: 56px; letter-spacing: -0.5px; }
  .card-front .brand-name { color: var(--text-dark); }
  .brand-tagline { font-size: 18px; margin-top: 4px; }
  .card-front .brand-tagline { color: var(--text-dark); }
  .front-stripe-orange {
    position: absolute; left: 0; right: 0; top: 300px; height: 8px;
    background: var(--accent-orange);
  }
  .front-stripe-grey {
    position: absolute; left: 0; right: 0; top: 312px; height: 3px;
    background: var(--line-grey);
  }
  .front-band {
    position: absolute; left: 0; right: 0; top: 320px; bottom: 0;
    background: var(--band-dark);
    display: flex; align-items: center; justify-content: center;
  }
  .front-website { color: var(--text-light); font-size: 34px; font-weight: 400; letter-spacing: 0.5px; }

  /* Back */
  .card-back { background: var(--card-dark); display: flex; }
  .back-brand {
    width: 420px; display: flex; flex-direction: column; align-items: center; justify-content: center;
    padding-left: 20px;
  }
  .card-back .brand-name { color: var(--text-light); font-size: 48px; }
  .card-back .brand-dot { width: 34px; height: 34px; }
  .card-back .brand-tagline { color: var(--text-muted); font-size: 16px; }
  .back-divider { width: 3px; margin: 40px 0; background: var(--accent-orange); }
  .back-contact { flex: 1; padding: 44px 0 0 26px; }
  .person-name { color: var(--accent-orange); font-size: 30px; font-weight: 400; letter-spacing: 0.5px; text-transform: uppercase; }
  .person-title { color: var(--text-muted); font-size: 17px; text-transform: uppercase; margin-top: 2px; }
  .contact-list { list-style: none; margin-top: 26px; }
  .contact-item {
    display: flex; align-items: flex-start; gap: 16px;
    color: var(--text-light); font-size: 16px; line-height: 1.35; margin-bottom: 14px;
  }
  .contact-icon { width: 22px; height: 22px; flex: none; }
</style>
</head>
<body>
<main class="canvas">

  <section class="card card-front" aria-label="Business card front">
    <div class="front-brand">
      <div class="brand-row">
        <span class="brand-dot"></span>
        <span class="brand-name">ParityLumen</span>
      </div>
      <p class="brand-tagline">Fairness Metrics Insight</p>
    </div>
    <div class="front-stripe-orange"></div>
    <div class="front-stripe-grey"></div>
    <div class="front-band">
      <p class="front-website">WWW.ParityLumen.com</p>
    </div>
  </section>

  <section class="card card-back" aria-label="Business card back">
    <div class="back-brand">
      <div class="brand-row">
        <span class="brand-dot"></span>
        <span class="brand-name">ParityLumen</span>
      </div>
      <p class="brand-tagline">Fairness Metrics Insight</p>
    </div>
    <div class="back-divider"></div>
    <div class="back-contact">
      <h1 class="person-name">Mara Ellison</h1>
      <p class="person-title">Chief Operating Officer</p>
      <ul class="contact-list">
        <li class="contact-item">
          <svg class="contact-icon" viewBox="0 0 24 24" aria-hidden="true"><path fill="#f7931e" d="M6.6 10.8a15 15 0 0 0 6.6 6.6l2.2-2.2c.3-.3.7-.4 1-.2 1.1.4 2.3.6 3.6.6.6 0 1 .4 1 1V20c0 .6-.4 1-1 1A17 17 0 0 1 3 4c0-.6.4-1 1-1h3.5c.6 0 1 .4 1 1 0 1.3.2 2.5.6 3.6.1.3 0 .7-.2 1z"/></svg>
          <span>(555) 014-2231</span>
        </li>
        <li class="contact-item">
          <svg class="contact-icon" viewBox="0 0 24 24" aria-hidden="true"><rect x="3" y="5" width="18" height="14" fill="none" stroke="#f7931e" stroke-width="2"/><path d="M3 6l9 7 9-7" fill="none" stroke="#f7931e" stroke-width="2"/></svg>
          <span>mara@paritylumen</span>
        </li>
        <li class="contact-item">
          <svg class="contact-icon" viewBox="0 0 24 24" aria-hidden="true"><circle cx="12" cy="12" r="9" fill="#f7931e"/></svg>
          <span>www.paritylumen.com</span>
        </li>
        <li class="contact-item">
          <svg class="contact-icon" viewBox="0 0 24 24" aria-hidden="true"><path d="M3 12l9-8 9 8M6 10v10h12V10" fill="none" stroke="#f7931e" stroke-width="2"/></svg>
          <span>78 Alder Row<br>Hollis Bay, ME<br>04021</span>
        </li>
        <li class="contact-item">
          <svg class="contact-icon" viewBox="0 0 24 24" aria-hidden="true"><rect x="4" y="4" width="16" height="16" fill="#f7931e"/></svg>
          <span>profile/paritylumen</span>
        </li>
        <li class="contact-item">
          <svg class="contact-icon" viewBox="0 0 24 24" aria-hidden="true"><rect x="4" y="4" width="16" height="16" fill="#f7931e"/></svg>
          <span>@paritylumen</span>
        </li>
      </ul>
    </div>
  </section>

</main>
</body>
</html>
```